Intenational Rhythmic Gymnastics Frostline Trophy

We need a poster for our new annual international rhythmic gymnastics competition "Frostline Trophy". Dates are December 21 -23, 2019.Picture we would like to use is attached.We would like to see holidays colors in the poster.It should have words "international rhythmic gymnastics", Name of the competition "Frostline Trophy" and dates.Also we would like for it to say somewhere that it is in Los Angeles, California, USAIt should have information about our club on the bottom of the poster like on the file attached (hosted by Venmarra Gymnastics with logo and address and website info)We also need a flyer that ties into the poster in look and colors with empty space below so we can add directives.We would like end product to be in file format that we can edit next year when the dates change.

Target Market(s)

Rhythmic Gymnastics Clubs

Industry/Entity Type

Gym

Colors

Designer to choose colors to be used in the design.

Requirements
Must have
• Picture we uploaded and all info we requested.
• Bright holiday colors

```html
<!DOCTYPE html>
<html lang="en">
<head>
<meta charset="utf-8">
<title>Frostline Trophy 2019 Poster</title>
<link rel="stylesheet" href="https://fonts.googleapis.com/css2?family=Cinzel:wght@400;500&family=Montserrat:wght@300;400;700&display=swap">
<style>
  :root {
    --stage: #a8c7da;
    --red-bright: #e0213d;
    --red-deep: #a01d33;
    --paper: #e7e7e7;
    --ink: #222222;
    --rule: #9a9a9a;
    --silver-light: #ffffff;
    --silver-dark: #b9b9bb;
  }
  * { margin: 0; padding: 0; box-sizing: border-box; }
  html, body {
    width: 1200px; height: 1200px; overflow: hidden;
    background: var(--stage);
    font-family: "Montserrat", Arial, sans-serif;
  }
  .poster {
    position: absolute; left: 197px; top: 30px;
    width: 806px; height: 1140px;
    background: var(--paper);
    overflow: hidden;
    box-shadow: 0 8px 24px rgba(0,0,0,0.25);
  }
  .poster__hero {
    position: absolute; left: 0; top: 0; width: 806px; height: 575px;
    background: radial-gradient(ellipse 70% 75% at 50% 78%, var(--red-bright) 0%, #c81f38 45%, var(--red-deep) 100%);
  }
  .poster__photo {
    position: absolute; left: 80px; top: 140px; width: 625px; height: 620px;
    background: radial-gradient(ellipse 45% 50% at 45% 58%, rgba(196,150,120,0.55) 0%, rgba(92,70,150,0.35) 45%, rgba(60,110,190,0.18) 70%, rgba(0,0,0,0) 100%);
  }
  .poster__floor-shadow {
    position: absolute; left: 40px; top: 748px; width: 726px; height: 14px;
    background: radial-gradient(ellipse 50% 50% at 50% 50%, rgba(0,0,0,0.45), rgba(0,0,0,0) 100%);
  }
  .poster__title {
    position: absolute; left: 0; top: 0; width: 806px; height: 460px;
  }
  .poster__kicker {
    font-family: "Cinzel", "Times New Roman", serif;
    font-size: 27px; fill: #ffffff;
  }
  .poster__name {
    font-family: "Cinzel", "Times New Roman", serif;
    font-weight: 500;
    fill: url(#silver);
    stroke: #8d8d90; stroke-width: 0.8;
    filter: url(#lift);
  }
  .poster__year {
    font-family: "Montserrat", Arial, sans-serif; font-weight: 400;
    fill: url(#silver); stroke: #8d8d90; stroke-width: 0.6;
    filter: url(#lift);
  }
  .poster__date {
    position: absolute; left: 0; top: 800px; width: 806px;
    text-align: center;
    font-weight: 300; font-size: 53px; color: var(--ink);
    letter-spacing: 0.5px;
  }
  .poster__date sup { font-size: 28px; vertical-align: 24px; margin-left: 2px; }
  .poster__venue {
    position: absolute; left: 247px; top: 881px; width: 288px; height: 37px;
    background: linear-gradient(90deg, var(--red-bright), var(--red-deep));
    color: #ffffff; font-size: 17px;
    display: flex; align-items: center; justify-content: center; gap: 5px;
  }
  .poster__venue strong { font-weight: 700; }
  .host {
    position: absolute; left: 118px; top: 985px; width: 595px;
    display: flex; align-items: center; gap: 18px;
    font-size: 16px; color: var(--ink);
  }
  .host__rule { flex: 1; height: 1px; background: var(--rule); }
  .club {
    position: absolute; left: 179px; top: 1045px;
    display: flex; align-items: center; gap: 10px;
    font-size: 20px; font-weight: 400; color: #1c2f6e;
  }
  .club__mark { width: 14px; height: 14px; border-radius: 50%; background: #1c2f6e; }
  .contact {
    position: absolute; left: 424px; top: 1036px;
    font-size: 11.5px; color: var(--ink);
    list-style: none;
  }
  .contact__item { display: flex; align-items: center; gap: 8px; height: 25px; }
  .contact__icon { width: 14px; height: 14px; flex: none; }
</style>
</head>
<body>
  <main class="poster">
    <div class="poster__hero"></div>
    <div class="poster__photo" role="img" aria-label="Photo of a rhythmic gymnast in a sparkling leotard in a deep lunge, swirling a blue and purple ribbon"></div>
    <div class="poster__floor-shadow"></div>

    <svg class="poster__title" viewBox="0 0 806 460" aria-label="International Rhythmic Gymnastics Frostline Trophy 2019">
      <defs>
        <linearGradient id="silver" x1="0" y1="0" x2="0" y2="1">
          <stop offset="0" stop-color="var(--silver-light)"/>
          <stop offset="0.55" stop-color="#e4e4e6"/>
          <stop offset="1" stop-color="var(--silver-dark)"/>
        </linearGradient>
        <filter id="lift" x="-5%" y="-10%" width="115%" height="130%">
          <feDropShadow dx="3" dy="4" stdDeviation="2.5" flood-color="#3a0a12" flood-opacity="0.55"/>
        </filter>
      </defs>
      <text class="poster__kicker" x="132" y="124" textLength="542" lengthAdjust="spacingAndGlyphs">INTERNATIONAL RHYTHMIC GYMNASTICS</text>
      <text class="poster__name" x="132" y="244" font-size="112" textLength="534" lengthAdjust="spacingAndGlyphs">FROSTLINE</text>
      <text class="poster__name" x="666" y="351" font-size="112" text-anchor="end" textLength="430" lengthAdjust="spacingAndGlyphs">TROPHY</text>
      <text class="poster__year" x="666" y="429" font-size="82" text-anchor="end" textLength="180" lengthAdjust="spacingAndGlyphs">2019</text>
    </svg>

    <p class="poster__date">December 21-23<sup>rd</sup></p>
    <p class="poster__venue">at <strong>Los Angeles, California</strong></p>

    <div class="host">
      <span class="host__rule"></span>
      <span class="host__label">Host by</span>
      <span class="host__rule"></span>
    </div>

    <div class="club">
      <span class="club__mark"></span>
      <span class="club__name">Venmarra Gymnastics</span>
    </div>

    <ul class="contact">
      <li class="contact__item">
        <svg class="contact__icon" viewBox="0 0 14 14" aria-hidden="true">
          <path d="M7 1a4.5 4.5 0 0 0-4.5 4.5C2.5 9 7 13.5 7 13.5S11.5 9 11.5 5.5A4.5 4.5 0 0 0 7 1z" fill="var(--red-bright)"/>
          <circle cx="7" cy="5.5" r="1.7" fill="#ffffff"/>
        </svg>
        4720 Larkspur Avenue, #212 Westbrook, CA 90412
      </li>
      <li class="contact__item">
        <svg class="contact__icon" viewBox="0 0 14 14" aria-hidden="true">
          <circle cx="7" cy="7" r="6" fill="none" stroke="var(--red-bright)" stroke-width="1.4"/>
          <ellipse cx="7" cy="7" rx="2.6" ry="6" fill="none" stroke="var(--red-bright)" stroke-width="1.1"/>
          <line x1="1" y1="7" x2="13" y2="7" stroke="var(--red-bright)" stroke-width="1.1"/>
          <line x1="2" y1="4" x2="12" y2="4" stroke="var(--red-bright)" stroke-width="0.9"/>
          <line x1="2" y1="10" x2="12" y2="10" stroke="var(--red-bright)" stroke-width="0.9"/>
        </svg>
        www.venmarragymnastics.com
      </li>
    </ul>
  </main>
</body>
</html>
```